KTNW Unique Letterhead for Financial Services Business

I am looking for a letterhead design to match our branding colours. I do not want to see anything generic that could be created in word, I can do that myself, I am after something with a bit of designer flair. Once completed I will need files in a print ready format (including bleed area).

I have included our logo file and also our new business card design but get creative.

Industry/Entity Type

Financial Services

Font styles to use
Other font styles liked:
• raleway

Colors
00AB8E
00BBA5
67D7C9
C6EFE9
E9F9F6

Requirements
Must have
• Must be consisten with logo branding colours.
Should not have
• Anything generic that I could create myself in word

```html
<!DOCTYPE html>
<html lang="en">
<head>
<meta charset="utf-8">
<title>KTNW Letterhead</title>
<link href="https://fonts.googleapis.com/css2?family=Open+Sans:wght@400;600&display=swap" rel="stylesheet">
<style>
  :root {
    --backdrop: #ececec;
    --paper: #ffffff;
    --ink: #3b3b3b;
    --ink-soft: #6a6a6a;
    --brand: #00AB8E;
    --brand-mid: #00BBA5;
    --brand-light: #67D7C9;
  }
  * { margin: 0; padding: 0; box-sizing: border-box; }
  html, body {
    width: 1200px; height: 795px; overflow: hidden;
    background: var(--backdrop);
    font-family: "Open Sans", Arial, sans-serif;
  }
  .letterhead {
    position: absolute; left: 330px; top: 16px;
    width: 540px; height: 763px;
    background: var(--paper);
    box-shadow: 0 2px 10px rgba(0,0,0,0.12);
    color: var(--ink);
  }
  .brand {
    position: absolute; left: 52px; top: 62px;
    display: flex; align-items: center; gap: 8px;
  }
  .brand-dot { width: 12px; height: 12px; border-radius: 50%; background: var(--brand); }
  .brand-name {
    font-size: 22px; font-weight: 400; letter-spacing: 3px; color: var(--brand);
  }
  .contact {
    position: absolute; right: 52px; top: 58px;
    font-size: 7px; line-height: 11px; color: var(--ink-soft);
    list-style: none;
  }
  .contact li { display: flex; align-items: center; gap: 5px; }
  .contact svg { width: 7px; height: 7px; fill: var(--brand); }
  .contact .spacer { width: 7px; }
  .letter-body {
    position: absolute; left: 52px; top: 190px; width: 436px;
    font-size: 9.5px; line-height: 13.5px; color: var(--ink-soft);
  }
  .salutation { font-size: 15px; color: var(--ink); margin-bottom: 12px; }
  .letter-body p { margin-bottom: 12px; }
  .closing { margin-top: 18px; }
  .signature {
    display: block; width: 70px; height: 30px; margin-top: 8px;
    background: linear-gradient(90deg, #e6e8ea, #f4f5f6);
    border-radius: 3px;
  }
  .accent-rule {
    position: absolute; left: 0; bottom: 0; width: 100%; height: 6px;
    background: linear-gradient(90deg, var(--brand), var(--brand-mid), var(--brand-light));
  }
</style>
</head>
<body>
  <main class="letterhead">
    <header class="brand">
      <span class="brand-dot"></span>
      <span class="brand-name">KTNW</span>
    </header>

    <ul class="contact">
      <li><span class="spacer"></span>PO Box 418 Elm Ridge NSW 2999</li>
      <li><svg viewBox="0 0 10 10"><path d="M2 1l2 0 1 2-1 1c.6 1.2 1.4 2 2.6 2.6l1-1 2 1v2c0 .5-.5 1-1 1C4 9.6.4 6 0 2c0-.5.5-1 1-1z"/></svg>0400 118 207</li>
      <li><svg viewBox="0 0 10 10"><rect x="0" y="2" width="10" height="6" rx="1"/></svg>info@ktnwfinance.example</li>
      <li><svg viewBox="0 0 10 10"><circle cx="5" cy="5" r="5"/></svg>www.ktnwfinance.example</li>
    </ul>

    <section class="letter-body">
      <h1 class="salutation" style="font-weight:400">Dear Mr. Harlow,</h1>
      <p>Lorem ipsum dolor sit amet, consectetur adipiscing elit. Donec orci purus, luctus vitae dignissim eu, iaculis sed purus. Vivamus faucibus, ipsum nec aliquet viverra, leo mauris condimentum ligula, sit amet sagittis enim ligula quis arcu. Nam egestas tortor id nisi porttitor mattis. In tortor ante, ultricies in suscipit a, tempus non massa. Vivamus et auctor mi. Fusce vel massa nulla. Phasellus nec eros mauris, et scelerisque orci.</p>
      <p>Donec malesuada orci vitae nulla accumsan porta a id massa. Quisque accumsan iaculis magna sit amet fringilla. Maecenas consequat, magna eget tincidunt semper, odio nibh rutrum mi, id feugiat ante nisi eu risus. Vestibulum nunc orci, rhoncus a placerat in, ultricies in mi. Cras mattis varius eros, vel fringilla nisi suscipit eget. Quisque scelerisque sagittis nulla at porttitor.</p>
      <p>Sed id augue vitae urna euismod commodo aliquet a quam. Pellentesque arcu velit, cursus et malesuada ut, consequat et diam. Nullam erat sem, rhoncus id ullamcorper vitae, rhoncus et arcu. In ultricies ultricies nulla, ut rutrum nisi iaculis at. Donec eu magna a metus ornare faucibus. Fusce aliquet faucibus ultricies. Morbi semper, est id tincidunt gravida, sem arcu adipiscing lacus, ac bibendum nulla leo eu purus. Quisque nec diam sed risus consectetur accumsan quis quis nibh. Vestibulum id purus lorem.</p>
      <p>It is a long established fact that a reader will be distracted by the readable content of a page when looking at its layout. The point of using Lorem Ipsum is that it has a more-or-less normal distribution of letters, as opposed to using 'Content here, content here', making it look like readable English. Many desktop publishing packages</p>
      <p class="closing">Sincerely,</p>
      <span class="signature" role="img" aria-label="Handwritten signature"></span>
    </section>

    <div class="accent-rule"></div>
  </main>
</body>
</html>
```